Tri-Fold Brochure Redesign for Floral Preservation Business

I would like to redesign my current tri-fold brouchue that I created myself and have it updated. I would like to keep the same content, color and images, but have it redesigned to look fresher and updated. I'm in the the floral preservation business and work with brides in the wedding inductry. I'm looking for a royal/rustic feel and it should relate to the look and feel of my website www.larkmeadowbloom.com. I have included the Photoshop file I used to create my orginal bouchure.

The only content that has changed is my address which is now;
4827 Maple Brook Lane, Reston VA 20194

Safe Zone Width - 10.875
Safe Zone Height - 8.375

I have included the Photoshop and Illustrator templates for the tri-fold brochure from the printer I will be using.

```html
<!DOCTYPE html>
<html lang="en">
<head>
<meta charset="utf-8">
<title>Lark Meadow Bloom – Tri-Fold Brochure, Outside Spread</title>
<link rel="stylesheet" href="https://fonts.googleapis.com/css2?family=Arimo:wght@400;700&family=Playfair+Display:ital,wght@1,700&family=Pinyon+Script&display=swap">
<style>
  :root {
    --stage: #5b5b5b;
    --panel-light: #ececec;
    --panel-white: #ffffff;
    --panel-grey-top: #dcdcdc;
    --panel-grey-bottom: #c9c9c9;
    --swirl: #e2e2e2;
    --swirl-white: #f4f4f4;
    --brand-red: #c8202f;
    --ink: #4a4a4a;
    --ink-soft: #5e5e5e;
    --link-blue: #1d4f8f;
  }
  * { box-sizing: border-box; margin: 0; padding: 0; }
  html, body { width: 1200px; height: 1000px; overflow: hidden; }
  body {
    background: var(--stage);
    font-family: "Arimo", Arial, sans-serif;
    color: var(--ink);
    position: relative;
  }
  .brochure {
    position: absolute;
    left: 40px; top: 184px;
    width: 1120px; height: 632px;
    display: grid;
    grid-template-columns: repeat(3, 1fr);
    box-shadow: 0 6px 24px rgba(0,0,0,.35);
  }
  .panel { position: relative; overflow: hidden; }
  .panel--about { background: var(--panel-light); padding: 0 34px; }
  .panel--contact { background: var(--panel-white); text-align: center; }
  .panel--cover { background: linear-gradient(180deg, var(--panel-grey-top), var(--panel-grey-bottom)); text-align: center; }

  .swirl-field {
    position: absolute; inset: 0;
    background: radial-gradient(ellipse at 30% 70%, var(--swirl) 0%, transparent 60%),
                radial-gradient(ellipse at 80% 20%, var(--swirl) 0%, transparent 55%);
    opacity: .8;
  }
  .panel--contact .swirl-field {
    background: radial-gradient(ellipse at 20% 30%, var(--swirl-white) 0%, transparent 60%),
                radial-gradient(ellipse at 75% 85%, var(--swirl-white) 0%, transparent 55%);
  }
  .panel > *:not(.swirl-field) { position: relative; }

  .brand {
    display: inline-flex; align-items: center; gap: 9px;
    font-family: "Arimo", Arial, sans-serif;
    font-weight: 400; color: var(--ink);
    white-space: nowrap;
  }
  .brand__mark { width: 26px; height: 26px; background: var(--brand-red); flex: none; }
  .brand__name { font-size: 22px; letter-spacing: .5px; }
  .brand--large .brand__mark { width: 34px; height: 34px; }
  .brand--large .brand__name { font-size: 28px; }

  .panel--about .brand { margin: 44px 0 0 70px; }
  .about__title {
    margin-top: 44px; text-align: center;
    color: var(--brand-red); font-weight: 700; font-size: 24px;
  }
  .flourish {
    display: block; margin: 8px auto 0;
    width: 110px; height: 22px; border-radius: 11px;
    background: linear-gradient(90deg, transparent, rgba(200,32,47,.55), transparent);
  }
  .about__body { margin-top: 12px; font-size: 12px; line-height: 1.45; color: var(--ink-soft); }
  .about__body p + p { margin-top: 14px; }
  .signature { margin-top: 10px; font-family: "Pinyon Script", cursive; font-size: 25px; color: var(--brand-red); }
  .signature__role { margin-top: 6px; font-size: 11px; line-height: 1.5; color: var(--ink-soft); }

  .panel--contact .brand { margin-top: 294px; }
  .contact__note { margin-top: 46px; color: var(--brand-red); font-size: 14px; }
  .contact__details { margin-top: 12px; font-size: 13.5px; line-height: 1.45; color: var(--ink); }
  .panel--contact .flourish { margin-top: 22px; }
  .social {
    margin: 20px auto 0; display: flex; align-items: center; justify-content: center; gap: 8px;
    color: var(--link-blue); font-weight: 700; font-size: 12.5px; line-height: 1.3; text-align: left;
  }
  .social__square { width: 42px; height: 42px; background: var(--link-blue); }
  .social__handle { margin-top: 12px; color: var(--link-blue); font-weight: 700; font-size: 12.5px; }

  .panel--cover .brand { margin-top: 84px; }
  .panel--cover .cover__frame {
    position: absolute; left: 32px; top: 258px; width: 308px; height: 196px;
    border-radius: 40%;
    background: radial-gradient(ellipse, rgba(255,255,255,.45) 0%, rgba(255,255,255,.15) 60%, transparent 75%);
  }
  .panel--cover .cover__tagline {
    position: absolute; left: 0; right: 0; top: 308px;
    font-family: "Playfair Display", Georgia, serif; font-style: italic; font-weight: 700;
    font-size: 19px; line-height: 1.2; color: var(--brand-red); letter-spacing: .3px;
  }
</style>
</head>
<body>
  <main class="brochure">
    <section class="panel panel--about">
      <div class="swirl-field" role="img" aria-label="Faint grey swirling vine pattern"></div>
      <div class="brand"><span class="brand__mark"></span><span class="brand__name">Lark Meadow Bloom</span></div>
      <h2 class="about__title">ABOUT US</h2>
      <span class="flourish" role="img" aria-label="Red decorative scroll ornament"></span>
      <div class="about__body">
        <p>With a rich family history in the floral business spanning over 60 years, I have spent the past two decades learning all aspects of the business but focusing primarily on perfecting the freeze-dry floral preservation process. Most recently I have expanded beyond the conventional freeze-dry offerings and have learned the art of creating flower petal jewelry from preserved flowers. I'm proud to be one of the few companies in the U.S. to offer this unique service.</p>
        <p>At Lark Meadow Bloom, we are committed to being the premiere floral preservation company in your community. I am extremely proud and honored to carry on the family name in the floral business by providing these services not only in my hometown of Washington DC but also in the Hampton Roads metro area. I'm confident the services offered by Lark Meadow Bloom are sure to exceed your expectations for years to come.</p>
      </div>
      <p class="signature">Evan Hollis</p>
      <p class="signature__role">Owner &amp; Operator<br>Lark Meadow Bloom</p>
    </section>

    <section class="panel panel--contact">
      <div class="swirl-field" role="img" aria-label="Faint white swirling vine pattern"></div>
      <div class="brand"><span class="brand__mark"></span><span class="brand__name">Lark Meadow Bloom</span></div>
      <p class="contact__note">BY APPOINTMENT ONLY</p>
      <p class="contact__details">4827 Maple Brook Lane, Reston VA 20194<br>703.555.0147 | www.larkmeadowbloom.com</p>
      <span class="flourish" role="img" aria-label="Red decorative scroll ornament"></span>
      <div class="social"><span class="social__square"></span><span>Become a fan and view<br>our most recent work</span></div>
      <p class="social__handle">@larkmeadowbloom</p>
    </section>

    <section class="panel panel--cover">
      <div class="swirl-field" role="img" aria-label="Faint grey swirling vine pattern"></div>
      <div class="brand brand--large"><span class="brand__mark"></span><span class="brand__name">Lark Meadow Bloom</span></div>
      <div class="cover__frame" role="img" aria-label="Ornate filigree frame surrounding the tagline"></div>
      <h1 class="cover__tagline">The National<br>Capital's Premier<br>Flower Preservation<br>Professionals</h1>
    </section>
  </main>
</body>
</html>
```